Lumaridge Hauling

WHY: So we are looking for a clean blue/modern/ mobile friendly website to be able compete with our rival, which is bellhops.comWHO: Our company is based out Atlanta,GA. The Company named is called "LumaRidge Hauling" and we are Professional staffing Agency that trained our employees for Household Industry related tasks such as Moving Furniture, Packers Household Boxes , Vondra Furniture Installers, Mounting TV and etc.WHAT: Our Main Function is we need to be able to pre-qualified lead/schedule them based on availability /Book our client online on Quenpay in order to help our client solve and their problem faster than the traditional 20 min phone call. We need an :Pre-Survey Form /Basic Contact Form Example Below...Desired Button Placement: Should be In the Center or Right Corner. * Q1. What would you like help with? (multi-Choice A to D?* Q2. What are you packing or unpacking* Q3. How many boxes would you like packed or unpacked?* Q4.In Additional to packing or unpacking, do you need any other service>* Q5. Would you like to add photos of the primary item you need packed on..* Q6. When would you like the packing specialist?* Q7. WHat time work best for your schedule?* Q8.Anything else the packing specialist should know? * Q8. Zip Code * Q9. Name* Q10. Email (Privacy Disclaimer)* Q12. Number * Q13. Customer Credit Card InfoWHEN: we looking to be done submit all of our revision request and the project done before New Year, Jan.1

Target Market(s)

Womans: Between 25yr to +55 Womans, Affluence,

Industry/Entity Type

Moving

Number of Pages Required

2 page

Font styles to use
Sans Serif

Colors

Designer to choose colors to be used in the design.

Requirements
Must have
• Service Option Category
• Packers/Installer/ Rental Trucks Assistant
• How it Work Session
• 1.Pick a Service
• 2.Book A Time
• 3.Secured A Payment
Nice to have
• Our Main Function is we need to be able to pre-qualified lead/schedule them based on availability /Book our client online on Quenpay in order to help our client solve and their problem faster than the traditional 20 min phone call.
• We need an :Pre-Survey Form /Basic Contact Form Example Below...
• Desired Button Placement: Should be In the Center or Right Corner.
• * Q1. What would you like help with? (multi-Choice A to D?
• * Q2. What are you packing or unpacking
• * Q3. How many boxes would you like packed or unpacked?
• * Q4.In Additional to packing or unpacking, do you need any other service>
• * Q5. Would you like to add photos of the primary item you need packed on..
• * Q6. When would you like the packing specialist?
• * Q7. WHat time work best for your schedule?
• * Q8.Anything else the packing specialist should know?
• * Q8. Zip Code
• * Q9. Name
• * Q10. Email (Privacy Disclaimer)
• * Q12. Number
• * Q13. Customer Credit Card Info
Should not have
• we are not interesting for an Basic Template Design /generic Truck photo stock/ traditional moving company website).

```html
<!DOCTYPE html>
<html lang="en">
<head>
<meta charset="utf-8">
<title>LumaRidge Hauling — Book a Local Mover</title>
<link rel="stylesheet" href="https://fonts.googleapis.com/css2?family=Roboto:wght@400;500;700;900&family=Open+Sans:ital,wght@0,400;0,600;0,700;1,400&display=swap">
<style>
:root{
  --orange:#e8742a;
  --orange-dark:#d9621b;
  --ink:#1b1b1b;
  --text:#555;
  --muted:#777;
  --grey-bg:#f4f4f4;
  --grey-band:#7d7d7d;
  --peach:#efc29c;
  --sand:#f3e6d2;
  --footer:#0d0d0d;
  --line:#dcdcdc;
  --white:#fff;
}
*{box-sizing:border-box;margin:0;padding:0}
html,body{width:1200px;height:4317px;overflow:hidden}
body{position:relative;background:var(--white);font-family:"Open Sans",sans-serif;color:var(--text)}
.abs{position:absolute}
.heading{font-family:"Roboto",sans-serif;font-weight:700;color:var(--ink);letter-spacing:.5px}
.btn-outline{position:absolute;display:flex;align-items:center;justify-content:center;border:2px solid var(--orange);border-radius:40px;color:var(--orange);font-family:"Roboto",sans-serif;font-weight:700;text-transform:uppercase;background:var(--white)}

/* top bar & nav */
.topbar{left:0;top:0;width:1200px;height:34px;background:var(--orange);color:var(--white);font-style:italic;font-weight:600;font-size:17px;display:flex;align-items:center;justify-content:center}
.brand{left:110px;top:60px;font-family:"Roboto",sans-serif;font-weight:900;font-size:29px;color:var(--ink);letter-spacing:-.5px}
.nav{left:430px;top:76px;display:flex;gap:38px;font-family:"Roboto",sans-serif;font-weight:500;font-size:15px;color:var(--ink);text-transform:uppercase}
.nav .active{color:var(--orange)}
.search{left:1074px;top:76px}

/* hero */
.hero-title{left:0;width:1200px;top:156px;text-align:center;font-size:44px}
.hero-art{left:14px;top:226px;width:500px;height:440px;border-radius:6px;background:linear-gradient(135deg,#ececec,#d8b48c 60%,#e07a3a)}
.hero-cut{left:0;top:560px}
.presurvey{left:518px;top:242px;width:190px;height:54px;font-size:15px}
.contact{left:725px;top:296px;width:363px;height:424px;background:var(--white);box-shadow:0 4px 18px rgba(0,0,0,.18)}
.contact-head{height:50px;background:#222;color:var(--white);font-family:"Roboto",sans-serif;font-weight:700;font-size:22px;display:flex;align-items:center;justify-content:center}
.field{margin:12px 24px 0;height:38px;border:1px solid var(--line);font-size:13px;color:#999;padding:9px 10px}
.field.msg{height:80px}
.submit{position:absolute;left:116px;top:320px;width:132px;height:46px;border-radius:30px;background:var(--orange);color:var(--white);font-family:"Roboto",sans-serif;font-weight:700;font-size:16px;display:flex;align-items:center;justify-content:center}
.next-arrow{left:1138px;top:396px}

/* what we do */
.wwd-art{left:43px;top:800px;width:446px;height:300px;border-radius:6px;background:linear-gradient(135deg,#f5f5f5,#d6d6d6 60%,#e9a06e)}
.wwd-title{left:590px;top:822px;font-size:42px}
.wwd-text{left:590px;top:900px;width:520px;font-size:14px;line-height:26px;color:var(--text)}
.wwd-btn{left:584px;top:1027px;width:271px;height:56px;font-size:15px}
.swoosh{left:0;top:1150px}

/* pricing */
.pricing-bg{left:0;top:1270px;width:1200px;height:745px;background:var(--grey-bg)}
.pricing-title{left:0;width:1200px;top:1344px;text-align:center;font-size:44px}
.card{position:absolute;background:var(--white);box-shadow:0 2px 10px rgba(0,0,0,.12);text-align:center}
.card-name{font-family:"Roboto",sans-serif;font-weight:700;font-size:22px;color:var(--ink);height:56px;display:flex;align-items:center;justify-content:center}
.card-price{height:46px;background:var(--grey-band);color:var(--white);font-family:"Roboto",sans-serif;font-weight:700;font-size:24px;display:flex;align-items:center;justify-content:center;gap:6px}
.card-price small{font-size:15px;font-weight:400}
.featured .card-price{background:var(--orange);height:58px}
.features{list-style:none;text-align:left;padding:20px 0 0 26px}
.features li{font-size:13px;color:var(--text);height:38px;display:flex;align-items:center;gap:10px}
.tick{width:15px;height:15px;border-radius:50%;background:var(--orange);flex:none;position:relative}
.tick::after{content:"";position:absolute;left:5px;top:2px;width:4px;height:7px;border:solid var(--white);border-width:0 2px 2px 0;transform:rotate(45deg)}
.book{position:relative;margin:20px auto 0;width:134px;height:42px;font-size:13px}

/* why us */
.why-panel{left:0;top:2023px}
.why-art{left:680px;top:2110px;width:470px;height:460px;border-radius:6px;background:linear-gradient(160deg,#f6f1ea,#e6a36b 55%,#3f6ea8)}
.why-title{left:110px;top:2100px;font-size:42px}
.why-item{position:absolute;left:110px;width:520px;height:92px}
.why-icon{position:absolute;left:0;top:0;width:92px;height:92px;border-radius:50%;border:2px solid var(--line);background:var(--white);display:flex;align-items:center;justify-content:center}
.why-item h3{position:absolute;left:114px;top:14px;font-family:"Roboto",sans-serif;font-weight:700;font-size:18px;color:var(--ink)}
.why-item p{position:absolute;left:114px;top:46px;font-size:13px;color:var(--text)}

/* testimonials */
.testi-title{left:0;width:1200px;top:2752px;text-align:center;font-size:44px}
.quote{left:250px;width:700px;top:2836px;text-align:center;font-style:italic;font-size:14px;line-height:26px;color:var(--muted)}
.author{left:0;width:1200px;top:2918px;text-align:center;font-family:"Roboto",sans-serif;font-weight:500;font-size:19px;color:var(--ink)}
.video{left:394px;top:2987px;width:412px;height:274px;background:linear-gradient(180deg,#8fc6ea 0%,#cfe6f3 55%,#e9b36a 75%,#8cab5a 100%);box-shadow:0 4px 14px rgba(0,0,0,.25)}
.play{left:572px;top:3096px}
.slide-arrow{top:3102px;width:46px;height:46px;border-radius:50%;border:2px solid #c9c9c9;display:flex;align-items:center;justify-content:center;background:var(--white)}

/* how it works */
.how-bg{left:0;top:3390px;width:1200px;height:640px;background:var(--sand)}
.how-title{left:0;width:1200px;top:3478px;text-align:center;font-size:44px}
.how-line{left:259px;top:3667px;width:685px;height:5px;background:#8a8a80}
.step{position:absolute;width:320px;text-align:center}
.step-circle{width:184px;height:184px;margin:0 auto;border-radius:50%;background:#cfc6b8;border:8px solid #8a8a80;display:flex;align-items:center;justify-content:center}
.step h3{margin-top:30px;font-family:"Roboto",sans-serif;font-weight:500;font-size:24px;color:var(--ink)}
.step p{margin:20px auto 0;width:300px;font-size:13px;line-height:24px;color:var(--muted)}

/* footer */
.footer{left:0;top:3960px}
.socials{left:0;width:1200px;top:4080px;display:flex;justify-content:center;gap:14px}
.social{width:46px;height:46px;border-radius:50%;border:2px solid var(--white)}
.contact-line{left:0;width:1200px;top:4166px;text-align:center;color:var(--white);font-size:14px;display:flex;justify-content:center;gap:18px;align-items:center}
.contact-line span{display:flex;align-items:center;gap:8px}
.links{left:0;width:1200px;top:4206px;display:flex;justify-content:center;gap:14px;color:var(--white);font-size:13px}
.copyright{left:0;width:1200px;top:4244px;text-align:center;color:var(--white);font-size:14px}
</style>
</head>
<body>

<div class="abs topbar">We get paid to sweat</div>
<div class="abs brand">LumaRidge Hauling</div>
<nav class="abs nav">
  <span class="active">Home</span><span>About Us</span><span>Service</span><span>Moving Services</span><span>Blog</span><span>Contact</span>
</nav>
<svg class="abs search" width="16" height="16" viewBox="0 0 16 16"><circle cx="6.5" cy="6.5" r="5" fill="none" stroke="#1b1b1b" stroke-width="2.2"/><line x1="10" y1="10" x2="15" y2="15" stroke="#1b1b1b" stroke-width="2.6"/></svg>

<!-- hero -->
<h1 class="abs heading hero-title">BOOK A LOCAL LUMARIDGE MOVER</h1>
<div class="abs hero-art" role="img" aria-label="Illustration of a mover unloading cardboard boxes from an open moving truck"></div>
<svg class="abs hero-cut" width="1200" height="180" viewBox="0 0 1200 180"><polygon points="0,160 1200,40 1200,180 0,180" fill="#fff"/></svg>
<div class="btn-outline presurvey">Pre-Survey</div>
<form class="abs contact">
  <div class="contact-head">CONTACT FORM</div>
  <div class="field">Name:</div>
  <div class="field">Email:</div>
  <div class="field">Phone No:</div>
  <div class="field msg">Message:</div>
  <div class="submit">SUBMIT</div>
</form>
<svg class="abs next-arrow" width="24" height="40" viewBox="0 0 24 40"><polyline points="4,4 20,20 4,36" fill="none" stroke="#fff" stroke-width="3"/></svg>

<!-- what we do -->
<div class="abs wwd-art" role="img" aria-label="Sketch of stacked moving boxes with a curved arrow"></div>
<h2 class="abs heading wwd-title">WHAT WE DO</h2>
<p class="abs wwd-text">At vero eos et accusamus et iusto odio dignissimos ducimus qui blanditiis pra esentium voluptatum deleniti atque corrupti quos dolores et quas molestiaex cepturi sint occaecati cupiditatemtique sunt.</p>
<div class="btn-outline wwd-btn">Let's get ready to move</div>
<svg class="abs swoosh" width="1200" height="120" viewBox="0 0 1200 120"><path d="M0,20 Q600,140 1200,15 L1200,42 Q600,150 0,48 Z" fill="#e8742a"/><path d="M0,48 Q600,150 1200,42 L1200,120 L0,120 Z" fill="#f4f4f4"/></svg>

<!-- pricing -->
<div class="abs pricing-bg"></div>
<h2 class="abs heading pricing-title">PRICING</h2>

<div class="card" style="left:110px;top:1485px;width:228px;height:400px">
  <div class="card-name">Packing Boxes</div>
  <div class="card-price">$30.00 <small>/ month</small></div>
  <ul class="features"><li><i class="tick"></i>Nam libero tempore cums</li><li><i class="tick"></i>Luta nobis est eligendi opt</li><li><i class="tick"></i>Nus id quod maxime pice</li><li><i class="tick"></i>Facere possim omnis volu</li><li><i class="tick"></i>Plas assumenda est, omni</li></ul>
  <div class="btn-outline book">Book Now!</div>
</div>
<div class="card featured" style="left:340px;top:1448px;width:270px;height:474px;z-index:2">
  <div class="card-name" style="height:62px">Moving Rental Truck</div>
  <div class="card-price">$130.00 <small>/ month</small></div>
  <ul class="features"><li><i class="tick"></i>Nam libero tempore cums</li><li><i class="tick"></i>Luta nobis est eligendi opt</li><li><i class="tick"></i>Nus id quod maxime pice</li><li><i class="tick"></i>Facere possim omnis volu</li><li><i class="tick"></i>Plas assumenda est, omni</li></ul>
  <div class="btn-outline book">Book Now!</div>
</div>
<div class="card" style="left:612px;top:1485px;width:228px;height:400px">
  <div class="card-name">POD/S</div>
  <div class="card-price">$230.00 <small>/ month</small></div>
  <ul class="features"><li><i class="tick"></i>Nam libero tempore cums</li><li><i class="tick"></i>Luta nobis est eligendi opt</li><li><i class="tick"></i>Nus id quod maxime pice</li><li><i class="tick"></i>Facere possim omnis volu</li><li><i class="tick"></i>Plas assumenda est, omni</li></ul>
  <div class="btn-outline book">Book Now!</div>
</div>
<div class="card" style="left:856px;top:1485px;width:232px;height:400px">
  <div class="card-name">Installation</div>
  <div class="card-price">$330.00 <small>/ month</small></div>
  <ul class="features"><li><i class="tick"></i>Nam libero tempore cums</li><li><i class="tick"></i>Luta nobis est eligendi opt</li><li><i class="tick"></i>Nus id quod maxime pice</li><li><i class="tick"></i>Facere possim omnis volu</li><li><i class="tick"></i>Plas assumenda est, omni</li></ul>
  <div class="btn-outline book">Book Now!</div>
</div>

<!-- why us -->
<svg class="abs why-panel" width="1200" height="602" viewBox="0 0 1200 602"><polygon points="762,0 1200,0 1200,602 524,602" fill="#efc29c"/></svg>
<div class="abs why-art" role="img" aria-label="Illustration of a mover in overalls carrying a box beside a loaded truck"></div>
<h2 class="abs heading why-title">WHY US</h2>

<div class="why-item" style="top:2173px">
  <div class="why-icon"><svg width="36" height="36" viewBox="0 0 36 36"><rect x="4" y="16" width="7" height="16" fill="#e8742a"/><path d="M13,16 L20,4 Q24,4 23,10 L22,15 L31,15 Q34,16 33,20 L30,30 Q29,32 26,32 L13,32 Z" fill="#e8742a"/></svg></div>
  <h3>Trusted Packers</h3><p>Nam libero tempoum soluta nobis est eligendi</p>
</div>
<div class="why-item" style="top:2276px">
  <div class="why-icon"><svg width="36" height="36" viewBox="0 0 36 36"><circle cx="15" cy="15" r="10" fill="none" stroke="#e8742a" stroke-width="4"/><line x1="22" y1="22" x2="32" y2="32" stroke="#e8742a" stroke-width="5" stroke-linecap="round"/></svg></div>
  <h3>Background check</h3><p>Nam libero tempoum soluta nobis est eligendi</p>
</div>
<div class="why-item" style="top:2378px">
  <div class="why-icon"><svg width="36" height="36" viewBox="0 0 36 36"><circle cx="18" cy="18" r="14" fill="none" stroke="#e8742a" stroke-width="4"/><polyline points="18,9 18,18 24,22" fill="none" stroke="#e8742a" stroke-width="3"/></svg></div>
  <h3>Same day availability</h3><p>Nam libero tempoum soluta nobis est eligendi</p>
</div>
<div class="why-item" style="top:2480px">
  <div class="why-icon"><svg width="36" height="36" viewBox="0 0 36 36"><circle cx="18" cy="18" r="11" fill="#e8742a"/><g stroke="#e8742a" stroke-width="4"><line x1="18" y1="2" x2="18" y2="34"/><line x1="2" y1="18" x2="34" y2="18"/><line x1="7" y1="7" x2="29" y2="29"/><line x1="29" y1="7" x2="7" y2="29"/></g></svg></div>
  <h3>Our Guarantee</h3><p>Nam libero tempoum soluta nobis est eligendi</p>
</div>

<!-- testimonials -->
<h2 class="abs heading testi-title">TESTIMONIALS</h2>
<p class="abs quote">" Nam libero tempore, cum soluta nobis est eligendi optio cumque nihil impedit quo minus id quod maxime placeat facere possimus, omnis voluptas assumenda est, omnis doendus "</p>
<div class="abs author">John Doe</div>
<div class="abs video" role="img" aria-label="Video still: illustrated delivery van arriving at a family home"></div>
<svg class="abs play" width="56" height="56" viewBox="0 0 56 56"><circle cx="28" cy="28" r="26" fill="#222"/><polygon points="22,16 40,28 22,40" fill="#fff"/></svg>
<div class="abs slide-arrow" style="left:271px"><svg width="14" height="14" viewBox="0 0 14 14"><polyline points="9,2 4,7 9,12" fill="none" stroke="#555" stroke-width="2"/></svg></div>
<div class="abs slide-arrow" style="left:878px"><svg width="14" height="14" viewBox="0 0 14 14"><polyline points="5,2 10,7 5,12" fill="none" stroke="#555" stroke-width="2"/></svg></div>

<!-- how it works -->
<div class="abs how-bg"></div>
<h2 class="abs heading how-title">HOW IT WORKS</h2>
<div class="abs how-line"></div>
<div class="step" style="left:99px;top:3577px">
  <div class="step-circle"><svg width="80" height="60" viewBox="0 0 80 60"><rect x="4" y="14" width="44" height="30" fill="#e8742a"/><path d="M48,22 L64,22 L74,34 L74,44 L48,44 Z" fill="#d9621b"/><circle cx="18" cy="48" r="7" fill="#333"/><circle cx="62" cy="48" r="7" fill="#333"/><circle cx="58" cy="16" r="12" fill="#fff" stroke="#333" stroke-width="3"/><polyline points="58,9 58,16 63,19" fill="none" stroke="#333" stroke-width="2.5"/></svg></div>
  <h3>Pick a Service</h3>
  <p>At vero eos et accusamus et iusto odio digniss imos ducimus qui blanditiis praesen</p>
</div>
<div class="step" style="left:439px;top:3577px">
  <div class="step-circle"><svg width="70" height="64" viewBox="0 0 70 64"><rect x="4" y="8" width="62" height="52" rx="4" fill="#fff" stroke="#333" stroke-width="3"/><rect x="4" y="8" width="62" height="13" fill="#3a8fd0"/><g fill="#e8742a"><rect x="12" y="27" width="8" height="7"/><rect x="26" y="27" width="8" height="7"/><rect x="40" y="27" width="8" height="7"/><rect x="54" y="27" width="6" height="7"/><rect x="12" y="40" width="8" height="7"/><rect x="26" y="40" width="8" height="7"/><rect x="40" y="40" width="8" height="7"/></g></svg></div>
  <h3>Book A Time</h3>
  <p>At vero eos et accusamus et iusto odio digniss imos ducimus qui blanditiis praesen</p>
</div>
<div class="step" style="left:784px;top:3577px">
  <div class="step-circle"><svg width="56" height="70" viewBox="0 0 56 70"><path d="M14,30 L14,20 Q14,6 28,6 Q42,6 42,20 L42,30" fill="none" stroke="#333" stroke-width="5"/><rect x="6" y="30" width="44" height="36" rx="4" fill="#f2b632" stroke="#333" stroke-width="3"/><circle cx="28" cy="45" r="5" fill="#333"/><rect x="26" y="47" width="4" height="10" fill="#333"/></svg></div>
  <h3>Secured a Payment</h3>
  <p>At vero eos et accusamus et iusto odio digniss imos ducimus qui blanditiis praesen</p>
</div>

<!-- footer -->
<svg class="abs footer" width="1200" height="357" viewBox="0 0 1200 357"><polygon points="0,70 1200,20 1200,357 0,357" fill="#7a5c3c"/><polygon points="0,78 1200,26 1200,357 0,357" fill="#0d0d0d"/></svg>
<div class="abs socials"><span class="social"></span><span class="social"></span><span class="social"></span><span class="social"></span></div>
<div class="abs contact-line">
  <span><svg width="10" height="14" viewBox="0 0 10 14"><path d="M5,0 Q10,0 10,5 Q10,8 5,14 Q0,8 0,5 Q0,0 5,0 Z" fill="#fff"/><circle cx="5" cy="5" r="2" fill="#0d0d0d"/></svg>Harlow Street, Ward 4, 3091 Fenmore Bay</span>|
  <span><svg width="13" height="13" viewBox="0 0 13 13"><path d="M2,0 L5,3 L3.5,5 Q5,8 8,9.5 L10,8 L13,11 L11,13 Q4,12 0,2 Z" fill="#fff"/></svg>+1 555 010 8888</span>|
  <span><svg width="14" height="10" viewBox="0 0 14 10"><rect width="14" height="10" fill="#fff"/><polyline points="0,0 7,6 14,0" fill="none" stroke="#0d0d0d" stroke-width="1.5"/></svg>info@lumaridgehauling.example</span>
</div>
<div class="abs links"><span>Help</span>|<span>FAQ</span>|<span>Support</span>|<span>Sitemap</span>|<span>Terms Of Use</span>|<span>Privacy Statement</span></div>
<div class="abs copyright">Copyright © 2018, LumaRidge Hauling.. All rights reserved.</div>

</body>
</html>
```